Falcon Letterhead

Looking for a design template for our company’s official letterheads & business cards.It has to be mainly white and include our company logo, website, social media handle, address, phone number. Visit our website to have an idea of our brand identity and colours. Please use the same font that we are using in our website.
Target Market(s)
Lubricants & Greases, Industrial markets, Automotive
Font styles to use
Other font styles liked:
- Saira Extra-Condensed
Colors
ffffff
000000
fbee3f
Requirements
Must have
- It must be consistent with our brand identity. It must use the same exact yellow (Pantone color: 102C) and black (Pantone color: K100) as our brand colors.
- Must also use our font attached (Saira.zip). It's called Saira Extra-Condensed.
- We intend to use the FALCON logo and not the small mini-FN logo.
- On the design we must include ALL of the following:
- E-mail: info@falconoils.example
- @FalconGreases
- www.falconoils.example
- Address: P.O. Boc 4728, Qurain 53004, Kuwait
- Phone: (+965) 24718395
- Gulf Marwa Oils logo (attached). The logo attached is in Blue/Red but you can select one solid color for all of it such as BLACK or YELLOW depending on what background color you'll select.
Nice to have
- Like it to be as professional and as modern as possible. It has look clean, slick and classy.
Should not have
- Too many different colors.

```html
<!DOCTYPE html>
<html lang="en">
<head>
<meta charset="utf-8">
<title>Falcon Letterhead</title>
<link rel="stylesheet" href="https://fonts.googleapis.com/css2?family=Saira+Extra+Condensed:wght@400;600;800&display=swap">
<style>
  :root {
    --brand-yellow: #fbee3f;
    --brand-black: #231f20;
    --paper: #ffffff;
    --stage: #d9d9d9;
    --fold-grey: #c4c4c4;
    --fold-grey-light: #dcdcdc;
    --ink-soft: #333333;
  }
  * { margin: 0; padding: 0; box-sizing: border-box; }
  html, body { width: 1200px; height: 784px; overflow: hidden; }
  body {
    background: var(--stage);
    font-family: "Saira Extra Condensed", "Arial Narrow", sans-serif;
    position: relative;
  }
  .letterhead {
    position: absolute;
    left: 345px;
    top: 32px;
    width: 509px;
    height: 720px;
    background: var(--paper);
    box-shadow: 0 6px 18px rgba(0,0,0,0.18);
    overflow: hidden;
  }
  .corner {
    position: absolute;
    display: block;
  }
  .corner--top { left: 0; top: 0; width: 200px; height: 120px; }
  .corner--bottom { right: 0; bottom: 0; width: 210px; height: 130px; }

  .brand-mark {
    position: absolute;
    left: 40px;
    top: 58px;
    background: var(--brand-yellow);
    border-radius: 8px;
    padding: 0 12px;
    height: 38px;
    display: flex;
    align-items: center;
  }
  .brand-mark__name {
    font-weight: 800;
    font-size: 34px;
    letter-spacing: 3px;
    color: var(--brand-black);
    line-height: 1;
  }

  .contact-list {
    position: absolute;
    left: 34px;
    bottom: 78px;
    list-style: none;
    font-size: 11px;
    color: var(--ink-soft);
    line-height: 1;
  }
  .contact-list__item {
    display: flex;
    align-items: center;
    gap: 7px;
    margin-bottom: 5px;
  }
  .contact-list__icon {
    width: 9px;
    height: 9px;
    flex: none;
  }

  .company-sign {
    position: absolute;
    left: 34px;
    bottom: 28px;
    display: flex;
    align-items: center;
    gap: 8px;
    white-space: nowrap;
  }
  .company-sign__dot {
    width: 24px;
    height: 24px;
    border-radius: 50%;
    background: var(--brand-black);
  }
  .company-sign__name {
    font-weight: 600;
    font-size: 14px;
    letter-spacing: 1px;
    color: var(--brand-black);
    text-transform: uppercase;
  }
</style>
</head>
<body>
  <main class="letterhead">
    <svg class="corner corner--top" viewBox="0 0 200 120" aria-hidden="true">
      <polygon points="70,0 200,0 200,0 110,70" fill="var(--brand-yellow)"/>
      <polygon points="0,0 70,0 110,70 0,40" fill="var(--brand-black)"/>
      <polygon points="0,40 110,70 20,60" fill="var(--fold-grey)"/>
      <polygon points="110,70 200,0 200,22" fill="var(--brand-yellow)"/>
    </svg>

    <div class="brand-mark">
      <span class="brand-mark__name">FALCON</span>
    </div>

    <ul class="contact-list">
      <li class="contact-list__item">
        <svg class="contact-list__icon" viewBox="0 0 10 10"><circle cx="5" cy="5" r="5" fill="var(--brand-yellow)"/><path d="M5 2.2a2 2 0 0 1 2 2c0 1.4-2 3.6-2 3.6S3 5.6 3 4.2a2 2 0 0 1 2-2z" fill="var(--paper)"/></svg>
        P.O. Boc 4728, Qurain 53004, Kuwait
      </li>
      <li class="contact-list__item">
        <svg class="contact-list__icon" viewBox="0 0 10 10"><circle cx="5" cy="5" r="5" fill="var(--brand-yellow)"/><rect x="3.5" y="2.2" width="3" height="5.6" rx="0.6" fill="var(--paper)"/></svg>
        (+965) 24718395
      </li>
      <li class="contact-list__item">
        <svg class="contact-list__icon" viewBox="0 0 10 10"><circle cx="5" cy="5" r="5" fill="var(--brand-yellow)"/><rect x="2.5" y="3.2" width="5" height="3.6" fill="var(--paper)"/></svg>
        info@falconoils.example
      </li>
      <li class="contact-list__item">
        <svg class="contact-list__icon" viewBox="0 0 10 10"><circle cx="5" cy="5" r="5" fill="var(--brand-yellow)"/><circle cx="5" cy="5" r="2" fill="none" stroke="var(--paper)" stroke-width="1"/></svg>
        @FalconGreases
      </li>
      <li class="contact-list__item">
        <svg class="contact-list__icon" viewBox="0 0 10 10"><circle cx="5" cy="5" r="5" fill="var(--brand-yellow)"/><circle cx="5" cy="5" r="2.4" fill="none" stroke="var(--paper)" stroke-width="0.9"/></svg>
        www.falconoils.example
      </li>
    </ul>

    <div class="company-sign">
      <span class="company-sign__dot"></span>
      <span class="company-sign__name">Gulf Marwa Oils Co.</span>
    </div>

    <svg class="corner corner--bottom" viewBox="0 0 210 130" aria-hidden="true">
      <polygon points="0,130 150,50 90,130" fill="var(--brand-yellow)"/>
      <polygon points="150,50 210,0 210,130" fill="var(--fold-grey-light)"/>
      <polygon points="150,50 210,130 90,130" fill="var(--brand-black)"/>
      <polygon points="150,50 210,0 185,70" fill="var(--fold-grey)"/>
    </svg>
  </main>
</body>
</html>
```